Vantor Advisory business card

Premium business card required
I have attached the brand as a powerpoint template but this can be made to look very up market, I have also attached my BIO for title reasons and to give you a feel for my skills
front of card
Derek Holloway
Managing Director Vantor Advisory
Retail, Customer-Led Experience, Transformation and Maximising Shareholder Return
Mobile +61(0)418557392
Email derekvantoradvisory.com
back of card

VANTOR ADVISORY’ OFFERING

We transform customer environments to extract benefits while elevating service levels;
We release millions of dollars in self-funding through continuous improvement;
We see CX as a key differentiator, proactively guarding share from market disrupters;
We re-invent service and create front-end of the future.

```html
<!DOCTYPE html>
<html lang="en">
<head>
<meta charset="utf-8">
<title>Vantor Advisory business card</title>
<link href="https://fonts.googleapis.com/css2?family=Noto+Serif:ital,wght@1,700&display=swap" rel="stylesheet">
<style>
  :root {
    --backdrop: #d4d4d4;
    --brand-blue: #1c82d6;
    --brand-blue-deep: #0b62b4;
    --charcoal: #3a3d3c;
    --charcoal-deep: #2f3231;
    --gold: #e2c73c;
    --ink: #1f2021;
    --paper: #ffffff;
  }
  * { box-sizing: border-box; margin: 0; padding: 0; }
  html, body {
    width: 1200px; height: 800px; overflow: hidden;
    background: var(--backdrop);
    font-family: "Noto Serif", Georgia, serif;
    font-style: italic; font-weight: 700;
  }
  .card {
    position: absolute; top: 284px;
    width: 430px; height: 238px; overflow: hidden;
    background: radial-gradient(ellipse at 45% 25%, var(--charcoal) 0%, var(--charcoal-deep) 85%);
  }
  .card--back { left: 110px; }
  .card--front { left: 638px; }

  .brand-band {
    height: 108px;
    background: radial-gradient(ellipse at 40% 20%, var(--brand-blue) 0%, var(--brand-blue-deep) 90%);
    display: flex; align-items: center; justify-content: center; gap: 14px;
  }
  .brand-name {
    color: var(--ink);
    font-size: 30px; letter-spacing: 0.5px;
  }
  .brand-dot {
    width: 48px; height: 48px; border-radius: 50%;
    background: var(--ink);
  }
  .offering {
    padding: 8px 30px 0;
    color: var(--paper);
    font-size: 12.4px; line-height: 15.5px;
  }
  .offering p {
    text-align: justify; text-align-last: center;
    margin-bottom: 7px;
  }

  .contact {
    text-align: center; color: var(--gold);
    padding-top: 44px;
  }
  .contact__name { font-size: 51px; line-height: 60px; letter-spacing: 0.3px; }
  .contact__title { font-size: 17.5px; margin-top: 12px; }
  .contact__phone { font-size: 17px; margin-top: 10px; }
  .contact__web { font-size: 15px; margin-top: 8px; }
</style>
</head>
<body>
  <section class="card card--back">
    <div class="brand-band">
      <span class="brand-name">Vantor Advisory</span>
      <span class="brand-dot" aria-hidden="true"></span>
    </div>
    <div class="offering">
      <p>We transform customer environments to extract benefits while elevating service levels.</p>
      <p>We release millions of dollars in self-funding through continuous improvement.</p>
      <p>We see CX as a key differentiator, proactively guarding share from market disrupters.</p>
    </div>
  </section>

  <section class="card card--front">
    <div class="contact">
      <h1 class="contact__name">Derek Holloway</h1>
      <p class="contact__title">Managing Director Vantor Advisory</p>
      <p class="contact__phone">Mobile: 61(0)418557392</p>
      <p class="contact__web">Derekvantoradvisory.com</p>
    </div>
  </section>
</body>
</html>
```